We need an eye catching logo design and Business Card that portrays our business, which is the cleaning and protecting of stainless steel with an organic non chemical product. This can be separate to the company name or can incorporate it. Maybe even just the company name itself. Company Name is Gleamwell Gleamwell.
Ideal for products exposed to weather elements, ie: balustrading, enclosures, BBQs, we also supply the product so you can do it yourself (DIY).
In addition we would want to include on this card:
1. My Name (Dean Horrocks)
2. Mobile No. (TBA Later)
3. Email address (TBA Later)
4. Web address (TBA Later)
Updates

Please note that we also need suggestions on a logo, as this we do not have this either.

Please note we have update our brief to be more specific.

Thank You.

Dean

Target Market(s)

Purchasing officers and government people.

Industry/Entity Type

Steel

Colors

Designer to choose colors to be used in the design.

Requirements
Must have
• 1. Name (Dean Horrocks)
2. Mobile No. (TBA Later)
Should not have
• Should not be to busy looking

```html
<!DOCTYPE html>
<html lang="en">
<head>
<meta charset="utf-8">
<title>Gleamwell Gleamwell – Business Card</title>
<link rel="stylesheet" href="https://fonts.googleapis.com/css2?family=Exo+2:wght@400;600&family=Saira+Semi+Condensed:wght@500;600&display=swap">
<style>
  :root {
    --steel-dark: #141414;
    --steel-mid: #2e2f31;
    --steel-light: #4a4b4e;
    --band-light: #6c6d70;
    --gold: #c9b37a;
    --text-light: #f2f2f2;
    --text-soft: #d8d8d8;
    --line: rgba(190, 190, 195, 0.55);
    --gap: #ffffff;
  }
  * { box-sizing: border-box; margin: 0; padding: 0; }
  html, body {
    width: 1041px; height: 1200px; overflow: hidden; background: var(--gap);
  }
  .canvas { position: relative; width: 1041px; height: 1200px; }

  .card {
    position: absolute; left: 0; width: 1041px; height: 577px; overflow: hidden;
    background:
      repeating-linear-gradient(0deg, rgba(255,255,255,0.025) 0 1px, rgba(0,0,0,0.04) 1px 3px),
      radial-gradient(ellipse 60% 55% at 50% 45%, var(--steel-light) 0%, var(--steel-mid) 45%, var(--steel-dark) 100%);
  }
  .card--front { top: 0; }
  .card--back { top: 623px; }

  /* Front */
  .front-band {
    position: absolute; left: 0; right: 0; top: 225px; height: 109px;
    background: linear-gradient(90deg, #3a3b3d 0%, var(--band-light) 50%, #3a3b3d 100%);
    border-top: 2px solid rgba(255,255,255,0.18);
    border-bottom: 2px solid rgba(0,0,0,0.5);
  }
  .brand-name {
    font-family: "Exo 2", sans-serif; font-weight: 600; color: var(--gold);
    text-transform: uppercase; white-space: nowrap; letter-spacing: 0.14em;
  }
  .front-band .brand-name {
    position: absolute; left: 0; right: 0; top: 50%; transform: translateY(-50%);
    text-align: center; font-size: 46px;
  }
  .website {
    position: absolute; left: 0; right: 0; top: 526px; text-align: center;
    font-family: "Exo 2", sans-serif; font-size: 21px; font-style: italic;
    letter-spacing: 0.28em; color: var(--text-soft);
  }

  /* Back */
  .rail-v { position: absolute; top: 0; bottom: 0; width: 3px; background: var(--line); }
  .rail-v--outer { left: 58px; }
  .rail-v--inner { left: 80px; }
  .rail-h { position: absolute; left: 0; right: 0; height: 3px; background: var(--line); }
  .rail-h--upper { top: 508px; }
  .rail-h--lower { top: 525px; }

  .card--back .brand-name {
    position: absolute; left: 109px; top: 60px; font-size: 34px;
  }
  .person-name {
    position: absolute; left: 0; right: 0; top: 236px; text-align: center;
    font-family: "Exo 2", sans-serif; font-weight: 400; font-size: 46px;
    color: var(--text-light);
  }
  .contact {
    position: absolute; display: flex; align-items: center; gap: 16px;
    font-family: "Saira Semi Condensed", sans-serif; color: var(--text-light);
  }
  .contact svg { fill: var(--text-light); flex: none; }
  .contact--email { left: 148px; top: 445px; font-size: 21px; font-weight: 500; }
  .contact--phone { left: 630px; top: 434px; font-size: 36px; font-weight: 600; }
</style>
</head>
<body>
<main class="canvas">
  <section class="card card--front">
    <div class="front-band">
      <div class="brand-name">Gleamwell Gleamwell</div>
    </div>
    <p class="website">www.gleamwellgleamwell.com.au</p>
  </section>

  <section class="card card--back">
    <span class="rail-v rail-v--outer"></span>
    <span class="rail-v rail-v--inner"></span>
    <span class="rail-h rail-h--upper"></span>
    <span class="rail-h rail-h--lower"></span>

    <div class="brand-name">Gleamwell Gleamwell</div>
    <h1 class="person-name">Dean Horrocks</h1>

    <p class="contact contact--email">
      <svg width="40" height="28" viewBox="0 0 40 28" aria-hidden="true">
        <path d="M0 0h40v28H0z M3 3v1l17 12L37 4V3z M3 7v18h34V7L20 19z" fill-rule="evenodd"/>
      </svg>
      gleamwellgleamwell1@inbox.au
    </p>
    <p class="contact contact--phone">
      <svg width="40" height="44" viewBox="0 0 40 44" aria-hidden="true">
        <g transform="rotate(-35 20 22)">
          <rect x="12" y="4" width="16" height="36" rx="3"/>
          <rect x="15" y="8" width="10" height="9" fill="#2e2f31"/>
          <rect x="15" y="21" width="3" height="3" fill="#2e2f31"/>
          <rect x="22" y="21" width="3" height="3" fill="#2e2f31"/>
          <rect x="15" y="27" width="3" height="3" fill="#2e2f31"/>
          <rect x="22" y="27" width="3" height="3" fill="#2e2f31"/>
        </g>
      </svg>
      0491 570 156
    </p>
  </section>
</main>
</body>
</html>
```